Redesign specialty cleaning services business brochure

I need a brochure re-designed and updated to reflect packages we sell for starting your own specialty cleaning business. We are a specialty cleaning company that has been in business for over 35 years and our company literature needs an update.The brochure needs to be a downloadable file as well as print-ready.The download will go on 2 of our websites https://dovrantco.com/ and http://tarvelbrookpolishinstitute.com/. I will attach the brochure that needs to be redesigned. They have not been updated for several years. I have new images to add to the updated brochure.
Colors
Designer to choose colors to be used in the design.
Look and feel
Each slider illustrates characteristics of the customer's brand and the style your logo design should communicate.

```html
<!DOCTYPE html>
<html lang="en">
<head>
<meta charset="utf-8">
<title>Kestrel Window Cleaning Package Brochure</title>
<link href="https://fonts.googleapis.com/css2?family=Mulish:wght@400;600;700;800&display=swap" rel="stylesheet">
<style>
  :root{
    --stage:#4a4a4a;
    --paper:#ffffff;
    --ink:#333333;
    --brand-blue:#0a4fa3;
    --accent-blue:#2f8ff0;
    --deep-blue:#0d3f86;
    --swoosh-grey:#c9cdd2;
    --pill-grey:#e6e7e9;
    --photo-a:#8a96a3;
    --photo-b:#c9c2b6;
    --photo-c:#3f5266;
  }
  *{margin:0;padding:0;box-sizing:border-box}
  html,body{width:727px;height:1200px;overflow:hidden;background:var(--stage)}
  body{font-family:"Mulish",sans-serif;position:relative}
  .brochure{position:absolute;left:23px;top:359px;width:680px;height:482px;background:var(--paper);overflow:hidden}
  .brochure-art{position:absolute;inset:0}
  .text{position:absolute;white-space:nowrap;line-height:1.15}
  .tagline{left:23px;top:29px;font-size:12px;color:var(--ink)}
  .title{left:22px;top:47px;font-size:24px;color:var(--ink);line-height:1.2}
  .title strong{display:block;font-weight:800;font-size:24.5px}
  .intro{left:23px;top:108px;font-size:10.8px;color:var(--ink);line-height:1.4}
  .offer{left:23px;top:142px;font-size:10.8px;font-weight:800;color:var(--ink)}
  .offer em{font-style:normal;color:var(--brand-blue)}
  .offer-note{left:23px;top:157px;font-size:9.3px;color:var(--ink)}
  .lead{left:24px;top:253px;font-size:9.8px;color:#fff}
  .feature{position:absolute;color:#fff}
  .feature h2{font-size:11.6px;font-weight:800;margin-bottom:4px;white-space:nowrap}
  .feature ul{list-style:none}
  .feature li{position:relative;padding-left:12px;font-size:9.6px;line-height:1.15;margin-bottom:3.5px;white-space:nowrap}
  .feature li::before{content:"";position:absolute;left:2px;top:2px;width:3px;height:6px;border:solid #fff;border-width:0 1.6px 1.6px 0;transform:rotate(45deg)}
  .feature.training{left:24px;top:272px}
  .feature.branding{left:24px;top:340px}
  .feature.branding li{margin-bottom:3.9px}
  .feature.equipment{left:256px;top:272px}
  .feature.equipment li{margin-bottom:6px}
  .feature.office{left:256px;top:362px}
  .feature.office li{margin-bottom:5px}
  .contact{position:absolute;top:369px;font-size:7.6px;color:#fff;text-align:right;line-height:1.3}
  .contact.person{right:112px}
  .contact.lines{right:17px}
  .web-pill{position:absolute;left:464px;top:424px;width:230px;height:32px;border-radius:16px 0 0 16px;background:linear-gradient(180deg,#fafafa,var(--pill-grey));padding-left:14px;display:flex;align-items:center;font-size:9.6px;font-weight:800;color:var(--ink)}
</style>
</head>
<body>
<main class="brochure">
  <svg class="brochure-art" viewBox="0 0 680 482" width="680" height="482" aria-hidden="false">
    <defs>
      <linearGradient id="photoTone" x1="0" y1="0" x2="1" y2="1">
        <stop offset="0" stop-color="var(--photo-b)"/>
        <stop offset=".5" stop-color="var(--photo-a)"/>
        <stop offset="1" stop-color="var(--photo-c)"/>
      </linearGradient>
      <linearGradient id="blueFade" x1="0" y1="0" x2="1" y2="0">
        <stop offset="0" stop-color="#0b55ad"/>
        <stop offset="1" stop-color="#0a4b9c"/>
      </linearGradient>
    </defs>
    <path d="M0,250 Q140,170 320,222 Q420,255 520,268 L680,270 L680,482 L0,482 Z" fill="var(--swoosh-grey)"/>
    <path d="M0,262 Q140,186 320,236 Q420,266 520,278 L680,280 L680,482 L0,482 Z" fill="var(--accent-blue)"/>
    <path d="M0,268 Q140,194 320,244 Q420,272 520,284 L680,286 L680,482 L0,482 Z" fill="url(#blueFade)"/>
    <path d="M273,0 Q290,190 420,258 L680,300 L680,0 Z" fill="var(--brand-blue)"/>
    <path d="M288,0 Q302,178 428,250 L680,290 L680,0 Z" fill="#fff"/>
    <path d="M292,0 L680,0 L680,288 Q560,300 470,265 Q320,200 292,0 Z" fill="url(#photoTone)" role="img" aria-label="Photo of window cleaners washing a storefront window with squeegee poles"/>
    <circle cx="382" cy="212" r="57" fill="#fff"/>
    <circle cx="382" cy="212" r="53" fill="url(#photoTone)" role="img" aria-label="Photo of a cleaner scrubbing soapy glass"/>
    <circle cx="491" cy="283" r="53" fill="#fff"/>
    <circle cx="491" cy="283" r="49" fill="url(#photoTone)" role="img" aria-label="Photo of a cleaner washing a house window"/>
    <circle cx="615" cy="286" r="58" fill="#fff"/>
    <circle cx="615" cy="286" r="54" fill="url(#photoTone)" role="img" aria-label="Photo of a squeegee wiping a window pane"/>
  </svg>

  <p class="text tagline">"Teaching Glass is Our Task"</p>
  <h1 class="text title">The 'Kestrel' Window<strong>Cleaning Package</strong></h1>
  <p class="text intro">The 'Kestrel' Startup Package is a complete 3 day<br>Window Cleaning System</p>
  <p class="text offer">Includes Training and Equipment for <em>Just $9,995.00</em></p>
  <p class="text offer-note">(Training for up 2 Team Members)</p>

  <p class="text lead">Here is just some of what you get;</p>

  <section class="feature training">
    <h2>Hands-on Window Cleaning Training</h2>
    <ul>
      <li>Basic Hands on Window Cleanig Training</li>
      <li>Ladder Safety Training Techniques</li>
      <li>Bidding &amp; Estimating Techiques</li>
    </ul>
  </section>

  <section class="feature branding">
    <h2>Company Branding Includes</h2>
    <ul>
      <li>3 page Website with 3 Months Free Hosting</li>
      <li>1 Logo Design</li>
      <li>2500 Door Hangers</li>
      <li>2500 Post Cards</li>
      <li>6 Uniform Shirt and Hats with Logo</li>
      <li>2(17.3" X 11.25") Magnetic Vehice Signs</li>
      <li>1 Designed Letterhead, Business Card &amp; Brochure</li>
    </ul>
  </section>

  <section class="feature equipment">
    <h2>Equipment Includes</h2>
    <ul>
      <li>1 Complete Window Cleaning<br>Bucket Bucket &amp; Tool Setup</li>
      <li>4 1/2 Piece Sectional Window<br>Cleaning Ladder Set</li>
    </ul>
  </section>

  <section class="feature office">
    <h2>Office Set-up</h2>
    <ul>
      <li>20 hours of Business Consulting</li>
      <li>Window Cleaning Marketing &amp;<br>Internet Advertising Plan</li>
    </ul>
  </section>

  <address class="contact person" style="font-style:normal">Dorian Vell<br>218 Marlow Crest Rd Ste 40<br>Fairbrook Ca. 95012</address>
  <address class="contact lines" style="font-style:normal">Ph. 555-310-2894<br>Fax. 555-310-2871<br>info@dovrantco.com</address>

  <p class="web-pill">www.tarvelbrookpolishinstitute.com</p>
</main>
</body>
</html>
```